a mobile app for beauty salon professional to publish their service and customers to book service

I plan to create an iPhone app (support iPhone 6 and above) that will allow beauty salon professionals (e.g. hair stylist) to publish their service/business with address/geolocation and available time slots, manage their professional profile with photos, and service charges, allow the customers to search services based on locations, and book the service. customer can provide feedback/ratings on the professional's service. a reference website : http://mira.tovelpa.example/booking/

Target Market(s)

beauty and hair salon professionals and customers

Industry/Entity Type

Hair And Beauty

Font styles to use
Sans Serif
Script

Colors

Designer to choose colors to be used in the design.

Requirements
Must have
• === customer features
• - user/customer registration
• - customer browse nearby service using a map view
• - customer browse nearby service using a list view ordered by distance (e.g. km)
• - customer search salon service based on service category, price range, and profressional's rating
• - customer select a service with zoom in details : salon name, service offered, location/address, and a "booking" button
• - customer place booking by specifying service (e.g. simple cut, blow-dry, etc) required, time slot, preferred professional
• - customer payments (paypal/credit card)
• - customer can feedback/rate on the salon professional
• === salon professional features
• - user/professional registration
• - maintain professional profile (private/public), option to upload photos
• - a registered professional can register/maintain shop/business who by default is the owner of the shop/business
• - a shop owner can assign professionals to the shop/business (multiple professional can work in the same location/shop)
• - professional maintain their service and schedule (breaks, holidays, working hours, appointments, service rates)

```html
<!DOCTYPE html>
<html lang="en">
<head>
<meta charset="utf-8">
<title>Salon Booking – Home</title>
<link rel="stylesheet" href="https://fonts.googleapis.com/css2?family=Inter:wght@200;300;400;600;700&display=swap">
<style>
  :root {
    --page-bg: #f8dbe9;
    --screen-bg: #ffffff;
    --ink: #2b2b2b;
    --ink-soft: #555555;
    --accent: #e8086f;
    --accent-light: #ff5a9c;
    --white: #ffffff;
    --card-shadow: rgba(60, 30, 50, 0.28);
  }
  * { box-sizing: border-box; margin: 0; padding: 0; }
  html, body {
    width: 1200px; height: 2273px; overflow: hidden;
    background: var(--page-bg);
    font-family: "Inter", "Helvetica Neue", Arial, sans-serif;
    color: var(--ink);
  }
  .canvas { position: relative; width: 1200px; height: 2273px; }
  .screen {
    position: absolute; left: 122px; top: 106px; width: 950px; height: 2014px;
    background: var(--screen-bg); border-radius: 56px; overflow: visible;
  }
  .abs { position: absolute; }

  /* status bar */
  .status { font-size: 20px; font-weight: 400; color: var(--ink-soft); top: 118px; }
  .status-carrier { left: 162px; display: flex; align-items: center; gap: 8px; }
  .status-time { left: 0; width: 1200px; text-align: center; font-weight: 600; }
  .status-battery { right: 162px; display: flex; align-items: center; gap: 8px; }

  /* header */
  .menu-button { left: 162px; top: 276px; }
  .location-label {
    left: 0; width: 1200px; text-align: center; top: 248px;
    font-size: 19px; font-weight: 600; color: var(--ink);
  }
  .location-current { left: 404px; top: 284px; display: flex; align-items: center; gap: 26px; }
  .location-name { font-size: 37px; font-weight: 400; color: var(--ink); }
  .search-button { left: 962px; top: 268px; }

  /* cards */
  .promo-card {
    position: absolute; left: 206px; width: 796px; height: 437px;
    border-radius: 32px; overflow: hidden;
    box-shadow: 0 34px 50px -14px var(--card-shadow);
  }
  .card-photo { position: absolute; inset: 0; }
  .photo-spa { background: linear-gradient(135deg, #c48aa9 0%, #e7b27a 40%, #d69ac0 70%, #b36fa2 100%); }
  .photo-nails { background: linear-gradient(120deg, #b7789e 0%, #e59fb0 45%, #c97aa0 75%, #9a5a86 100%); }
  .photo-hair { background: linear-gradient(110deg, #d78eaa 0%, #b9789a 40%, #e4a4bd 70%, #c985a8 100%); }

  .card-title {
    position: absolute; left: 38px; font-size: 54px; font-weight: 200;
    color: var(--white); letter-spacing: -0.5px; line-height: 1;
  }
  .card-subtitle {
    position: absolute; font-size: 37px; font-weight: 700;
    color: var(--white); line-height: 1;
  }
  .offer-value {
    position: absolute; left: 36px; top: 212px; font-size: 86px; font-weight: 200;
    color: var(--white); line-height: 1; letter-spacing: -2px;
  }
  .offer-label {
    position: absolute; left: 40px; top: 300px; font-size: 37px; font-weight: 700;
    color: var(--white); line-height: 1;
  }
  .book-button {
    position: absolute; left: 38px; top: 365px; width: 216px; height: 54px;
    border-radius: 27px; background: var(--white); color: var(--accent);
    font-size: 29px; font-weight: 700; display: flex; align-items: center; justify-content: center;
  }
  .add-button {
    position: absolute; width: 128px; height: 128px; left: 857px; border-radius: 50%;
    background: linear-gradient(160deg, var(--accent-light), var(--accent));
    box-shadow: 0 18px 30px -8px rgba(232, 8, 111, 0.45);
    display: flex; align-items: center; justify-content: center;
  }
</style>
</head>
<body>
<div class="canvas">
  <div class="screen"></div>

  <div class="abs status status-carrier">
    <svg width="62" height="14" viewBox="0 0 62 14" aria-hidden="true">
      <circle cx="7" cy="7" r="6" fill="#555"/><circle cx="19" cy="7" r="6" fill="#555"/><circle cx="31" cy="7" r="6" fill="#555"/>
      <circle cx="43" cy="7" r="5.3" fill="none" stroke="#555" stroke-width="1.4"/><circle cx="55" cy="7" r="5.3" fill="none" stroke="#555" stroke-width="1.4"/>
    </svg>
    <span>mobile</span>
    <svg width="24" height="18" viewBox="0 0 24 18" aria-hidden="true">
      <path d="M2 6a14 14 0 0 1 20 0M6 10a8 8 0 0 1 12 0" fill="none" stroke="#555" stroke-width="2.4" stroke-linecap="round"/>
      <circle cx="12" cy="15" r="2.4" fill="#555"/>
    </svg>
  </div>
  <div class="abs status status-time">4:21 PM</div>
  <div class="abs status status-battery">
    <svg width="12" height="20" viewBox="0 0 12 20" aria-hidden="true">
      <path d="M2 6l8 8-4 4V2l4 4-8 8" fill="none" stroke="#777" stroke-width="1.6"/>
    </svg>
    <span>100%</span>
    <svg width="42" height="18" viewBox="0 0 42 18" aria-hidden="true">
      <rect x="1" y="1" width="36" height="16" rx="3" fill="none" stroke="#555" stroke-width="1.5"/>
      <rect x="3.5" y="3.5" width="31" height="11" rx="1.5" fill="#555"/>
      <rect x="38.5" y="6" width="2.5" height="6" rx="1" fill="#555"/>
    </svg>
  </div>

  <svg class="abs menu-button" width="90" height="36" viewBox="0 0 90 36" aria-label="Menu">
    <rect x="0" y="6" width="74" height="8" rx="4" fill="#333"/>
    <rect x="0" y="26" width="58" height="8" rx="4" fill="#333"/>
    <circle cx="80" cy="7" r="7" fill="var(--accent)"/>
  </svg>

  <div class="abs location-label">Change your Location</div>
  <div class="abs location-current">
    <svg width="18" height="26" viewBox="0 0 18 26" aria-hidden="true">
      <path d="M9 0a9 9 0 0 1 9 9c0 7-9 17-9 17S0 16 0 9a9 9 0 0 1 9-9z" fill="var(--accent)"/>
      <circle cx="9" cy="9" r="3.5" fill="#fff"/>
    </svg>
    <span class="location-name">Sydney, Australia</span>
  </div>

  <svg class="abs search-button" width="48" height="48" viewBox="0 0 48 48" aria-label="Search">
    <circle cx="19" cy="19" r="14" fill="none" stroke="#2b2b2b" stroke-width="6"/>
    <line x1="29" y1="29" x2="43" y2="43" stroke="#2b2b2b" stroke-width="8" stroke-linecap="round"/>
  </svg>

  <section class="promo-card" style="top:424px">
    <div class="card-photo photo-spa" role="img" aria-label="Spa setting with a yellow hibiscus flower on rolled white towels"></div>
    <h2 class="card-title" style="top:58px">Mira's Salon</h2>
    <p class="card-subtitle" style="left:124px;top:117px">Season offer</p>
    <p class="offer-value">40%</p>
    <p class="offer-label">Discount</p>
    <div class="book-button">Book Now</div>
  </section>

  <section class="promo-card" style="top:952px">
    <div class="card-photo photo-nails" role="img" aria-label="Hand with painted nail designs, polka dots and flowers"></div>
    <h2 class="card-title" style="top:56px">Nail Design</h2>
    <p class="card-subtitle" style="left:99px;top:125px">Your Choice</p>
  </section>
  <div class="add-button" style="top:1326px" aria-label="Add nail design">
    <svg width="46" height="46" viewBox="0 0 46 46" aria-hidden="true">
      <rect x="19" y="2" width="8" height="42" rx="4" fill="#fff"/><rect x="2" y="19" width="42" height="8" rx="4" fill="#fff"/>
    </svg>
  </div>

  <section class="promo-card" style="top:1481px">
    <div class="card-photo photo-hair" role="img" aria-label="Stylist blow-drying long hair with a round brush"></div>
    <h2 class="card-title" style="top:56px">Hair Style</h2>
    <p class="card-subtitle" style="left:68px;top:115px">Best Stylist</p>
  </section>
  <div class="add-button" style="top:1856px" aria-label="Add hair style">
    <svg width="46" height="46" viewBox="0 0 46 46" aria-hidden="true">
      <rect x="19" y="2" width="8" height="42" rx="4" fill="#fff"/><rect x="2" y="19" width="42" height="8" rx="4" fill="#fff"/>
    </svg>
  </div>
</div>
</body>
</html>
```